Quillrests.com website overhaul

We want to upgrade our Wix website into a professional looking page for our growing business. The content that is online now needs to be used but the site should have a new look and feel from top to bottom. QuillRests is a company in the hospital and nursing home space. We would like to see the website use our color scheme but other than that we are open to any and all ideas. www.quillrests.com

```html
<!DOCTYPE html>
<html lang="en">
<head>
<meta charset="utf-8">
<title>QuillRests – Source-Focused HEPA Filtration</title>
<link href="https://fonts.googleapis.com/css2?family=Exo+2:wght@500;600;700&family=Montserrat:wght@300;400;500;600;700&family=Mulish:wght@300;400;500&display=swap" rel="stylesheet">
<style>
  :root{
    --ink:#2a1860;
    --indigo:#4753a4;
    --indigo-btn:#4651a0;
    --deep:#2c1a58;
    --footer-bar:#2b1150;
    --body:#333340;
    --muted:#8a8a96;
    --band:#f1f1f4;
    --line:#c9c9d2;
    --white:#ffffff;
  }
  *{box-sizing:border-box;margin:0;padding:0}
  html,body{width:1200px;height:3350px;overflow:hidden;background:var(--white)}
  body{position:relative;font-family:"Mulish",sans-serif;color:var(--body)}
  .abs{position:absolute}

  /* nav */
  .nav{left:0;top:0;width:1200px;height:104px;background:var(--white)}
  .nav a{position:absolute;top:40px;font:400 16px "Mulish",sans-serif;color:#333;text-decoration:none}
  .nav a.active{font-weight:700;color:var(--ink)}
  .nav .dot{position:absolute;left:163px;top:29px;width:7px;height:7px;background:var(--ink);transform:rotate(45deg)}
  .brand{display:flex;align-items:center;gap:10px;font:700 28px "Exo 2",sans-serif;color:var(--ink)}
  .brand .mark{width:22px;height:22px;background:var(--indigo)}
  .nav .brand{position:absolute;left:500px;top:32px}

  /* hero */
  .hero{left:0;top:104px;width:1200px;height:533px;background:var(--band)}
  .hero .welcome{left:146px;top:178px;font:400 28px "Exo 2",sans-serif;color:var(--indigo)}
  .hero h1{position:absolute;left:144px;top:208px;font:700 66px "Exo 2",sans-serif;color:var(--indigo);letter-spacing:-0.5px}
  .btn{position:absolute;display:flex;align-items:center;justify-content:center;gap:10px;background:var(--indigo-btn);color:var(--white);border-radius:22px;font:400 14px "Mulish",sans-serif}
  .video{left:560px;top:108px;width:580px;height:316px;border-radius:20px;background:linear-gradient(180deg,#3e62c0,#4059b0 70%,#5a64b4)}
  .video .play{position:absolute;left:252px;top:130px;width:56px;height:56px}

  /* protection */
  .section-title{font:600 34px/40px "Exo 2",sans-serif;color:var(--ink)}
  .intro-title{left:146px;top:730px;width:500px}
  .intro-text{left:148px;top:838px;width:485px;font:400 16px/27.3px "Mulish",sans-serif;text-align:justify;color:#333}
  .intro-art{left:692px;top:772px;width:364px;height:266px;border-radius:8px;background:linear-gradient(180deg,#4753a4 0 10px,#d4dce6 10px,#cfd9e4 85%,#d7a98b 85%)}

  .center{left:0;width:1200px;text-align:center}
  .sub{font:400 16px "Mulish",sans-serif;color:var(--ink)}

  /* feature cards */
  .card{left:147px;width:911px;background:var(--indigo);color:var(--white)}
  .card .strip{position:absolute;top:0;width:161px;height:100%;background:var(--deep)}
  .card h3{position:absolute;font:600 34px "Exo 2",sans-serif}
  .card p{position:absolute;font:300 16px/25.7px "Mulish",sans-serif;text-align:justify}

  /* pdf band */
  .pdf{left:0;top:2097px;width:1200px;height:280px;background:var(--band)}

  /* contact */
  .contact-photo{left:0;top:2448px;width:431px;height:540px;background:linear-gradient(160deg,#9aa6b8,#c9b7ae 55%,#7d8698)}
  .contact h2{position:absolute;left:480px;top:2462px;font:600 34px "Montserrat",sans-serif;color:var(--ink)}
  .contact .lead{position:absolute;left:480px;top:2516px;width:600px;font:400 14.5px/27px "Montserrat",sans-serif;color:#333}
  .field{position:absolute;height:48px;border:1px solid #9a9aa8;border-radius:24px;padding:0 16px;display:flex;align-items:center;font:400 14px "Montserrat",sans-serif;color:var(--muted)}
  .field.focus{border:2px solid #1fa5e6}
  .field.msg{height:102px;border-radius:51px}
  .submit{left:480px;top:2932px;width:596px;height:48px;border-radius:24px;font:500 15px "Montserrat",sans-serif}

  /* footer */
  .footbar{left:0;top:3053px;width:1200px;height:40px;background:var(--footer-bar)}
  .footbar span{position:absolute;top:10px;font:400 16px "Mulish",sans-serif;color:var(--white)}
  .foot .brand{position:absolute;left:146px;top:3170px}
  .foot-links{left:401px;top:3145px;font:400 16px/24px "Mulish",sans-serif;color:#333}
  .vdiv{width:1px;height:112px;background:var(--line)}
  .foot-info{font:400 16px/32px "Mulish",sans-serif;color:#222}
  .foot-info .row{display:flex;align-items:center;gap:12px;height:38px}
  .foot-info svg{width:16px;height:16px}
  .rule{left:0;top:3282px;width:1200px;height:1px;background:var(--line)}
  .copy{top:3303px;font:400 12px "Mulish",sans-serif;color:#555}
</style>
</head>
<body>

<header class="abs nav">
  <span class="dot"></span>
  <a class="active" style="left:146px">Home</a>
  <a style="left:260px">How it Works</a>
  <div class="brand"><span class="mark"></span>QuillRests</div>
  <a style="left:857px">Resources</a>
  <a style="left:1000px">Contact</a>
</header>

<section class="abs hero">
  <div class="abs welcome">Welcome to</div>
  <h1>QuillRests</h1>
  <div class="btn" style="left:146px;top:302px;width:162px;height:40px">Get Started</div>
  <div class="abs video" role="img" aria-label="Video still: a clinician beside a patient resting in a hospital bed">
    <svg class="play" viewBox="0 0 56 56"><circle cx="28" cy="28" r="26" fill="#fff" opacity=".95"/><circle cx="28" cy="28" r="22" fill="#3e5cb8"/><path d="M22 17 L39 28 L22 39 Z" fill="#fff"/></svg>
  </div>
</section>

<section>
  <h2 class="abs section-title intro-title">Enhanced Parotection Against Airborne Infectious Particles</h2>
  <p class="abs intro-text">The QuillRest is an air filtration system that reduces the exposure to airborne infectious particles for healthcare workers, patients, and visitors by utilizing a source-focused technology that captures airborne infectious particles at the source. The QuillRest utilizes a patent-pending headboard design that pulls air from the head area of the patient through a HEPA filtration system and exhausts filtered air back into the room.</p>
  <div class="btn" style="left:147px;top:1056px;width:162px;height:40px">Read More</div>
  <div class="abs intro-art" role="img" aria-label="Illustration: hospital bed with a headboard filtration unit drawing air away from the patient"></div>
</section>

<section>
  <h2 class="abs section-title center" style="top:1163px">Source-Focused HEPA Filtration</h2>
  <p class="abs sub center" style="top:1221px">Capture airborne infectious particles at the source</p>

  <article class="abs card" style="top:1270px;height:330px">
    <div class="strip" style="left:0"></div>
    <h3 style="left:212px;top:35px">Greater Protection than an N95 Mask*</h3>
    <p style="left:212px;top:90px;width:637px">According to the NHRA Study, "Expedient Methods for Surge Airborne Isolation within Healthcare Settings during Response to a Natural or Manmade Epidemic", the expedient airborne isolation research discussed within this document has identified isolation configurations that rely upon inexpensive, off-the-shelf materials and HEPA filtration systems that are commonly found within healthcare facilities. Most provide better real-time source protection from infectious aerosol than that expected to result from an N95 respirator. In several cases, the protection is several times better. *based on standard source focused air filtration cited in above named study available on our resources page.</p>
  </article>

  <article class="abs card" style="top:1630px;height:176px">
    <div class="strip" style="right:0"></div>
    <h3 style="left:57px;top:37px">Deploys in Minutes</h3>
    <p style="left:58px;top:92px;width:660px;text-align:left">The QuillRest is a complete system that can be deployed in a matter of minutes using only basic tools. The system easily disassembles for sanitation.</p>
  </article>

  <article class="abs card" style="top:1835px;height:176px">
    <div class="strip" style="right:0"></div>
    <h3 style="left:56px;top:37px">9 Minutes</h3>
    <p style="left:58px;top:92px;width:660px;text-align:left">Turns over air in a 15 x 20 room in 9 minutes.</p>
  </article>
</section>

<section class="abs pdf">
  <h2 class="abs section-title center" style="top:66px">QuillRests PDF Quick Info Sheet</h2>
  <p class="abs sub center" style="top:124px">Quick download for a printable information piece on the QuillRests system.</p>
  <div class="btn" style="left:357px;top:180px;width:167px;height:38px">
    <svg width="16" height="16" viewBox="0 0 16 16" fill="none" stroke="#fff" stroke-width="1.5"><path d="M8 2v8M4.5 6.5 8 10l3.5-3.5M2 11v3h12v-3"/></svg>Download PDF</div>
  <div class="btn" style="left:564px;top:180px;width:280px;height:38px">
    <svg width="14" height="16" viewBox="0 0 14 16" fill="none" stroke="#fff" stroke-width="1.3"><rect x="1.5" y="1" width="11" height="14" rx="1"/><path d="M4 5h6M4 8h6M4 11h4"/></svg>QuillRests PDF Quick Info Sheet</div>
</section>

<section class="contact">
  <div class="abs contact-photo" role="img" aria-label="Photo: hands holding a smartphone with phone, mail and email symbols above"></div>
  <h2>Get In Touch</h2>
  <p class="lead">Lorem ipsum dolor sit amet, consectetur adipiscing elit, sed do eiusmod tempor incididunt ut labore et dolore magna aliqua.</p>
  <div class="field focus" style="left:480px;top:2590px;width:282px">First Name</div>
  <div class="field" style="left:793px;top:2590px;width:283px">Last Name</div>
  <div class="field" style="left:480px;top:2663px;width:596px">Email</div>
  <div class="field" style="left:480px;top:2734px;width:596px">Phone</div>
  <div class="field msg" style="left:480px;top:2806px;width:596px">Message</div>
  <div class="btn submit">Submit</div>
</section>

<footer class="foot">
  <nav class="abs footbar">
    <span style="left:333px">Home</span>
    <span style="left:461px">How It Works</span>
    <span style="left:636px">Resources</span>
    <span style="left:786px">Contact Us</span>
  </nav>
  <div class="brand"><span class="mark"></span>QuillRests</div>
  <div class="abs foot-links">Privacy Policy<br>About Us<br>Support<br>Terms &amp; Conditions</div>
  <div class="abs vdiv" style="left:566px;top:3140px"></div>
  <div class="abs foot-info" style="left:607px;top:3142px">
    <div style="display:flex;gap:14px">
      <svg width="14" height="18" viewBox="0 0 14 18" style="margin-top:8px"><path d="M7 0a7 7 0 0 0-7 7c0 5 7 11 7 11s7-6 7-11a7 7 0 0 0-7-7z" fill="#222"/><circle cx="7" cy="7" r="2.5" fill="#fff"/></svg>
      <div>1, Sample Street,<br>Sample City<br>USA - 23543</div>
    </div>
  </div>
  <div class="abs vdiv" style="left:797px;top:3140px"></div>
  <div class="abs foot-info" style="left:830px;top:3134px">
    <div class="row"><svg viewBox="0 0 16 16" fill="none" stroke="#222" stroke-width="1.4"><path d="M3 1.5h3l1.5 3.5-2 1.2a8 8 0 0 0 4.3 4.3l1.2-2 3.5 1.5v3c0 .6-.5 1-1 1A13 13 0 0 1 2 2.5c0-.5.4-1 1-1z"/></svg>302-555-0148</div>
    <div class="row"><svg viewBox="0 0 16 16"><rect x="1" y="3" width="14" height="10" rx="1" fill="#222"/><path d="M1.5 4 8 9l6.5-5" fill="none" stroke="#fff" stroke-width="1.2"/></svg>hello@quillrests.com</div>
    <div class="row"><svg viewBox="0 0 16 16" fill="none" stroke="#222" stroke-width="1.4"><circle cx="8" cy="8" r="6.5"/><path d="M1.5 8h13M8 1.5c-3 3.5-3 9.5 0 13M8 1.5c3 3.5 3 9.5 0 13"/></svg>www.quillrests.com</div>
  </div>
  <div class="abs rule"></div>
  <p class="abs copy center">© copyrights 2022 &nbsp;Quillrests | &nbsp;All Rights Reserved</p>
</footer>

</body>
</html>
```